MAPLEWREN HOUSE DECOR

We need a web design for a new business based in Bonny Hills (NSW). We are a small retail outlet on the Mid North Coast (NSW, Australia) selling home wares, gifts, beach wear, artwork, and hampers etc. We would like to a few different samples if that's not too much trouble (e.g. black and white vs colour, e.g. "beach colours").
We would like the website to communicate that we are an affordable, local (community based) business, with customer satisfaction at the forefront of our mind. We have a strong customer service focus, and in addition to retail sales we are now looking to expand into the online hamper business.
We are open 7 days (except public holidays).
Note: We like the design / layout of the "Lamp Crest 'N' Shelf Website" if you would like to compare www.lampcrestnshelf.com.au

```html
<!DOCTYPE html>
<html lang="en">
<head>
<meta charset="utf-8">
<title>Maplewren House Decor</title>
<link rel="stylesheet" href="https://fonts.googleapis.com/css2?family=Lato:wght@400;700;900&family=Questrial&display=swap">
<style>
:root{
  --teal:#7ccbdc;
  --teal-dark:#3fb2cb;
  --orange:#e0963a;
  --sand:#f7c46f;
  --yellow:#f6c25f;
  --aqua:#a9e4ed;
  --pale:#d8eaf0;
  --ink:#333333;
  --grey:#7d7d7d;
  --white:#ffffff;
}
*{margin:0;padding:0;box-sizing:border-box}
html,body{width:941px;height:1200px;overflow:hidden;background:var(--white)}
body{position:relative;font-family:'Lato',sans-serif;color:var(--ink)}
.abs{position:absolute}

.topbar{left:0;top:0;width:941px;height:23px;background:var(--teal)}
.toplinks{right:109px;top:7px;font-size:8px;font-weight:700;color:var(--white);letter-spacing:.3px}
.toplinks span{margin:0 6px}

.brand{left:109px;top:40px;font-family:'Questrial',sans-serif;font-size:27px;color:#3a3a3a;letter-spacing:.3px;white-space:nowrap}
.tagline{left:123px;top:71px;font-family:'Questrial',sans-serif;font-size:15px;color:var(--grey);letter-spacing:.6px;white-space:nowrap}
.cart-text{left:737px;top:36px;font-size:8px;font-weight:700;color:#666;line-height:12px}
.cart-icon{left:808px;top:35px;width:24px;height:22px;background:#e6e6e6}
.search{left:627px;top:72px;width:205px;height:27px;border:1px solid #d2d2d2;border-radius:3px;background:#fafafa}
.search span{position:absolute;left:7px;top:6px;font-size:11px;font-style:italic;color:#9a9a9a}
.search svg{position:absolute;right:7px;top:6px}

.nav{left:0;top:112px;width:941px;height:36px;background:var(--orange)}
.nav-home{left:112px;top:108px;width:68px;height:40px;background:var(--ink);border-radius:3px 3px 0 0}
.nav-item{top:123px;font-size:11.5px;font-weight:700;color:var(--white);transform:translateX(-50%);white-space:nowrap}
.nav-sep{top:118px;width:1px;height:24px;background:rgba(255,255,255,.45)}

.hero{left:0;top:148px;width:941px;height:267px;background:linear-gradient(100deg,#6b5a4e 0%,#9a8c83 30%,#c9c3bd 55%,#e4e1de 75%,#b06b6a 100%)}
.hero-caption{left:528px;top:306px;width:304px;height:84px;background:rgba(120,200,215,.35)}
.hero-text{right:115px;top:308px;text-align:right;font-size:22.5px;line-height:30px;color:var(--white);white-space:nowrap}
.dot{top:376px;width:14px;height:4px;background:var(--white)}

.main{left:0;top:415px;width:941px;height:457px;background:var(--pale)}
.feature{top:430px;height:141px;padding:5px;background:var(--white)}
.feature .inner{position:relative;width:100%;height:100%}
.feature .label{position:absolute;left:11px;top:40px;font-size:10px;color:var(--ink)}
.feature .title{position:absolute;left:11px;top:55px;font-size:16.5px;line-height:21px;color:var(--white);white-space:nowrap}
.feature svg{position:absolute;right:12px;top:26px}

.section-title{left:0;width:941px;top:595px;text-align:center;font-size:17px;color:var(--ink)}
.rule{top:606px;height:1px;background:#aac8cc}

.card{top:638px;width:142px;height:195px;background:var(--white);border-radius:4px;box-shadow:0 1px 3px rgba(0,0,0,.12)}
.card .photo{position:absolute;left:6px;top:6px;width:130px;height:120px;border:1px solid #eee}
.card .name{position:absolute;left:0;width:100%;top:137px;text-align:center;font-size:13px;font-weight:700;color:var(--teal-dark)}
.card .line{position:absolute;left:14px;width:114px;top:157px;height:1px;background:#e5e5e5}
.card .blurb{position:absolute;left:0;width:100%;top:164px;text-align:center;font-size:9.3px;line-height:13px;font-weight:700;color:#777}

.ship-text{left:196px;top:907px;font-size:17.5px;font-weight:900;color:var(--ink);white-space:nowrap}
.badge{left:738px;top:888px}

.footer{left:0;top:964px;width:941px;height:202px;background:var(--ink)}
.f-head{top:985px;font-size:12px;color:var(--teal);padding-bottom:5px;border-bottom:1px solid var(--orange);width:96px;white-space:nowrap}
.f-links{top:1016px;font-size:9.5px;font-weight:700;color:var(--white);line-height:22.3px;white-space:nowrap}
.f-note{left:294px;top:1017px;font-size:10px;color:var(--white);line-height:15px;width:170px}
.f-input{left:293px;width:166px;height:20px;background:#f4f4f4}
.f-input span{position:absolute;left:6px;top:5px;font-size:8.5px;font-style:italic;color:#999}
.f-btn{left:293px;top:1108px;width:68px;height:21px;background:var(--teal);color:var(--white);font-size:9px;font-weight:900;text-align:center;line-height:21px}
.social{left:744px;width:22px;height:22px}
.social-label{left:782px;font-size:10px;color:var(--white)}

.bottombar{left:0;top:1166px;width:941px;height:34px;background:var(--teal)}
.copy{left:107px;top:1178px;font-size:9.5px;font-weight:700;color:var(--white)}
.bottom-brand{right:110px;top:1173px;font-family:'Questrial',sans-serif;font-size:17px;color:var(--white);white-space:nowrap}
</style>
</head>
<body>

<div class="abs topbar"></div>
<div class="abs toplinks">SIGN IN<span>|</span>REGISTER<span>|</span>CHECKOUT</div>

<div class="abs brand">Maplewren House Decor</div>
<div class="abs tagline">home ware . kitchen ware . linen . gifts</div>

<div class="abs cart-text">SHOPPING CART<br>ITEMS (05)</div>
<div class="abs cart-icon">
  <svg width="24" height="22" viewBox="0 0 24 22"><path d="M5 6h2l2 8h8l2-6H8" fill="none" stroke="#555" stroke-width="1.4"/><circle cx="10" cy="17" r="1.3" fill="#555"/><circle cx="16" cy="17" r="1.3" fill="#555"/></svg>
</div>
<div class="abs search"><span>Search</span>
  <svg width="15" height="15" viewBox="0 0 15 15"><circle cx="6" cy="6" r="4.5" fill="none" stroke="#333" stroke-width="1.8"/><path d="M9.5 9.5l4 4" stroke="#333" stroke-width="2"/></svg>
</div>

<div class="abs nav"></div>
<div class="abs nav-home"></div>
<div class="abs nav-item" style="left:146px">Home</div>
<div class="abs nav-item" style="left:245px">Home Ware</div>
<div class="abs nav-sep" style="left:310px"></div>
<div class="abs nav-item" style="left:377px">Kitchen Ware</div>
<div class="abs nav-sep" style="left:445px"></div>
<div class="abs nav-item" style="left:491px">Linen</div>
<div class="abs nav-sep" style="left:540px"></div>
<div class="abs nav-item" style="left:583px">Gifts</div>
<div class="abs nav-sep" style="left:623px"></div>
<div class="abs nav-item" style="left:685px">About Us</div>
<div class="abs nav-sep" style="left:743px"></div>
<div class="abs nav-item" style="left:803px">Contact Us</div>

<div class="abs hero" role="img" aria-label="Shop interior with cookware, glassware, linen and cushions on display"></div>
<div class="abs hero-caption"></div>
<div class="abs hero-text">We Have A Strong Customer<br>Service Focus</div>
<div class="abs dot" style="left:720px;background:var(--orange)"></div>
<div class="abs dot" style="left:742px"></div>
<div class="abs dot" style="left:764px"></div>
<div class="abs dot" style="left:786px"></div>
<div class="abs dot" style="left:808px"></div>

<div class="abs main"></div>

<div class="abs feature" style="left:108px;width:238px;background:#5bc0d9">
  <div class="inner" style="background:var(--white);padding:4px"><div class="inner" style="background:var(--teal-dark)">
    <div class="label">LOCAL</div>
    <div class="title">COMMUNITY<br>PRODUCTS</div>
    <svg width="86" height="74" viewBox="0 0 86 74" fill="#333">
      <circle cx="43" cy="14" r="10"/><circle cx="16" cy="28" r="9"/><circle cx="70" cy="28" r="9"/>
      <rect x="30" y="26" width="26" height="26" rx="8"/><rect x="4" y="38" width="24" height="24" rx="8"/><rect x="58" y="38" width="24" height="24" rx="8"/>
      <path d="M14 60q29 20 58 0" fill="none" stroke="#333" stroke-width="5"/>
    </svg>
  </div></div>
</div>

<div class="abs feature" style="left:353px;width:236px;background:#e59a3e">
  <div class="inner" style="background:var(--white);padding:4px"><div class="inner" style="background:var(--sand)">
    <div class="label">BEST</div>
    <div class="title">CUSTOMER<br>SATISFACTION</div>
    <svg width="80" height="80" viewBox="0 0 84 84" style="top:22px;right:10px">
      <circle cx="42" cy="42" r="37" fill="#333"/>
      <path d="M24 43l12 12 24-26" fill="none" stroke="#f7c46f" stroke-width="8" stroke-linecap="round" stroke-linejoin="round"/>
    </svg>
  </div></div>
</div>

<div class="abs feature" style="left:596px;width:237px;background:var(--yellow)">
  <div class="inner" style="background:var(--white);padding:4px"><div class="inner" style="background:var(--aqua)">
    <div class="label">EXCLUSIVES</div>
    <div class="title">STORE OPEN<br>ALL 7 DAYS</div>
    <svg width="86" height="84" viewBox="0 0 86 84">
      <rect x="4" y="10" width="64" height="60" rx="6" fill="#333"/>
      <rect x="14" y="2" width="7" height="16" rx="3" fill="#333" stroke="#a9e4ed" stroke-width="2"/>
      <rect x="50" y="2" width="7" height="16" rx="3" fill="#333" stroke="#a9e4ed" stroke-width="2"/>
      <g fill="#a9e4ed"><rect x="12" y="28" width="9" height="8"/><rect x="25" y="28" width="9" height="8"/><rect x="38" y="28" width="9" height="8"/><rect x="51" y="28" width="9" height="8"/><rect x="12" y="41" width="9" height="8"/><rect x="25" y="41" width="9" height="8"/><rect x="12" y="54" width="9" height="8"/><rect x="25" y="54" width="9" height="8"/></g>
      <circle cx="64" cy="60" r="18" fill="#333" stroke="#a9e4ed" stroke-width="3"/>
      <path d="M64 49v12h8" fill="none" stroke="#a9e4ed" stroke-width="3"/>
    </svg>
  </div></div>
</div>

<div class="abs rule" style="left:109px;width:265px"></div>
<div class="abs section-title">OUR PRODUCTS</div>
<div class="abs rule" style="left:565px;width:267px"></div>

<svg class="abs" style="left:90px;top:720px" width="20" height="38" viewBox="0 0 20 38"><path d="M17 2L3 19l14 17" fill="none" stroke="#9fb8bd" stroke-width="1.5"/></svg>
<svg class="abs" style="left:831px;top:720px" width="20" height="38" viewBox="0 0 20 38"><path d="M3 2l14 17L3 36" fill="none" stroke="#9fb8bd" stroke-width="1.5"/></svg>

<div class="abs card" style="left:136px">
  <div class="photo" role="img" aria-label="Table lamps and a white vase" style="background:linear-gradient(180deg,#ffffff,#ece6dc)"></div>
  <div class="name">Home Ware</div><div class="line"></div>
  <div class="blurb">Lorem ipsum dolor sit<br>amet, consectetuer adipis</div>
</div>
<div class="abs card" style="left:311px">
  <div class="photo" role="img" aria-label="Colourful kitchen utensils and bowls" style="background:linear-gradient(180deg,#ffffff,#e9d8d4)"></div>
  <div class="name">Kitchen Ware</div><div class="line"></div>
  <div class="blurb">Lorem ipsum dolor sit<br>amet, consectetuer adipis</div>
</div>
<div class="abs card" style="left:486px">
  <div class="photo" role="img" aria-label="Folded striped tea towels tied with ribbon" style="background:linear-gradient(180deg,#ffffff,#d6ecee)"></div>
  <div class="name">Linen</div><div class="line"></div>
  <div class="blurb">Lorem ipsum dolor sit<br>amet, consectetuer adipis</div>
</div>
<div class="abs card" style="left:662px">
  <div class="photo" role="img" aria-label="Red gift hamper basket with treats" style="background:linear-gradient(180deg,#ffffff,#f0d4cf)"></div>
  <div class="name">Gifts</div><div class="line"></div>
  <div class="blurb">Lorem ipsum dolor sit<br>amet, consectetuer adipis</div>
</div>

<svg class="abs" style="left:108px;top:898px" width="54" height="38" viewBox="0 0 54 38">
  <rect x="1" y="3" width="32" height="24" rx="2" fill="#4a4a4a"/>
  <path d="M35 10h10l7 9v8H35z" fill="#4a4a4a"/>
  <rect x="38" y="13" width="7" height="6" fill="#fff"/>
  <circle cx="11" cy="30" r="5" fill="#4a4a4a" stroke="#fff" stroke-width="2"/>
  <circle cx="43" cy="30" r="5" fill="#4a4a4a" stroke="#fff" stroke-width="2"/>
  <text x="17" y="19" text-anchor="middle" font-family="Lato,sans-serif" font-size="9" font-weight="900" fill="#fff">FREE</text>
</svg>
<div class="abs ship-text">WE OFFER FREE SHIPPING FOR ORDERS OF $100 OR MORE</div>
<svg class="abs badge" width="94" height="60" viewBox="0 0 94 60">
  <polygon points="47,1 54,6 63,3 67,9 77,8 78,15 87,17 85,24 93,30 85,36 87,43 78,45 77,52 67,51 63,57 54,54 47,59 40,54 31,57 27,51 17,52 16,45 7,43 9,36 1,30 9,24 7,17 16,15 17,8 27,9 31,3 40,6" fill="#7ccbdc"/>
  <text x="47" y="22" text-anchor="middle" font-family="Lato,sans-serif" font-size="7" font-weight="900" fill="#fff">WE HAVE A</text>
  <text x="47" y="31" text-anchor="middle" font-family="Lato,sans-serif" font-size="7" font-weight="900" fill="#fff">FLAT RATE SHIPPING</text>
  <text x="47" y="43" text-anchor="middle" font-family="Lato,sans-serif" font-size="10" font-weight="900" fill="#fff">OF $6.95.</text>
</svg>

<div class="abs footer"></div>
<div class="abs f-head" style="left:107px;width:92px">Quick Links</div>
<div class="abs f-links" style="left:109px">About Us<br>Blog<br>Delivery<br>Information<br>Privacy Policy<br>Terms &amp; Conditons</div>

<div class="abs f-head" style="left:292px;width:166px">Signup For Newsletter</div>
<div class="abs f-note">Signup with us and get update in your inbox.</div>
<div class="abs f-input" style="top:1051px"><span>Your Name</span></div>
<div class="abs f-input" style="top:1079px"><span>Email address</span></div>
<div class="abs f-btn">SUBSCRIBE</div>

<div class="abs f-head" style="left:554px;width:96px">Customer Service</div>
<div class="abs f-links" style="left:559px">Contact Us<br>Returns<br>Site Map<br>Privacy Policy<br>Terms &amp; Conditions</div>

<div class="abs f-head" style="left:744px;width:88px">Follow Us On</div>
<div class="abs social" style="top:1020px;background:#3b5a98"></div>
<div class="abs social-label" style="top:1025px">Townsquare</div>
<div class="abs social" style="top:1050px;background:#2fa9e0"></div>
<div class="abs social-label" style="top:1055px">Chirpline</div>
<div class="abs social" style="top:1080px;background:#c4302b"></div>
<div class="abs social-label" style="top:1085px">Clipstream</div>
<div class="abs social" style="top:1110px;background:#0e76a8"></div>
<div class="abs social-label" style="top:1115px">Workweb</div>

<div class="abs bottombar"></div>
<div class="abs copy">© MaplewrenHouseDecor 2014. All Rights Reserved.</div>
<div class="abs bottom-brand">Maplewren House Decor</div>

</body>
</html>
```